Solar panel cleaning flyer design.

I'm looking for a flyer design for my new company called Brightfield Panel Works. We are a South Australian company that professionally clean residential and commercial solar panels. We generate leads by going door to door and need a flyer to hand out to our customers if they are interested in our service. As we are a new company we don't have anything particular in mind so be creative! Must include the company name and logo.

```html
<!DOCTYPE html>
<html lang="en">
<head>
<meta charset="utf-8">
<title>Brightfield Panel Works – Flyer</title>
<link href="https://fonts.googleapis.com/css2?family=Open+Sans:wght@400;600;700;800&display=swap" rel="stylesheet">
<style>
  :root {
    --green: #7dbb2a;
    --green-dark: #4f9a1c;
    --green-light: #a9d24a;
    --blue: #1f6fb8;
    --blue-dark: #15528f;
    --grey-text: #5d5d5d;
    --footer: #3b3b3b;
    --white: #ffffff;
    --page: #f2f2f2;
  }
  * { margin: 0; padding: 0; box-sizing: border-box; }
  html, body { width: 826px; height: 1200px; overflow: hidden; background: var(--page); }
  body { font-family: "Open Sans", Arial, sans-serif; }
  .flyer { position: relative; width: 826px; height: 1200px; background: var(--white); overflow: hidden; }
  .flyer-shapes { position: absolute; inset: 0; }
  .block { position: absolute; }

  .headline { left: 455px; top: 108px; white-space: nowrap; color: var(--green); font-weight: 700; font-size: 52px; line-height: 1.1; }
  .subline { left: 455px; top: 178px; white-space: nowrap; color: var(--grey-text); font-weight: 600; font-size: 21px; line-height: 1.2; }
  .intro-copy { left: 440px; top: 245px; width: 355px; color: var(--white); font-size: 15px; line-height: 1.45; }

  .contact-label { left: 460px; top: 425px; white-space: nowrap; color: var(--green-dark); font-weight: 700; font-size: 46px; line-height: 1.1; }
  .contact-phone { left: 460px; top: 480px; white-space: nowrap; color: var(--grey-text); font-weight: 600; font-size: 58px; line-height: 1.1; letter-spacing: 1px; }

  .feature-title { left: 40px; top: 590px; width: 400px; color: var(--white); font-weight: 700; font-size: 58px; line-height: 1.05; }
  .feature-copy { left: 40px; top: 762px; width: 360px; color: var(--white); font-size: 15px; line-height: 1.45; }

  .brand { left: 500px; top: 625px; width: 300px; display: flex; flex-direction: column; align-items: center; gap: 10px; }
  .brand-mark { width: 58px; height: 58px; border-radius: 50%; background: var(--blue); }
  .brand-name { color: var(--blue-dark); font-weight: 700; font-size: 26px; text-align: center; line-height: 1.1; }

  .bulb-art { left: 560px; top: 770px; width: 200px; height: 320px; border-radius: 45% 45% 30% 30%;
    background: radial-gradient(circle at 50% 40%, #e9f3d0 0%, #b8d98a 40%, #cfd6dc 75%, #ffffff 100%); }

  .services-title { left: 30px; top: 920px; white-space: nowrap; color: var(--white); font-weight: 700; font-size: 36px; line-height: 1.2; }
  .service-photo { top: 975px; width: 120px; height: 120px; border-radius: 50%; border: 5px solid var(--white); }
  .service-photo.home { left: 40px; background: radial-gradient(circle at 50% 40%, #f4d7a8, #c98a4a 70%, #8a5a2a); }
  .service-photo.roof { left: 205px; background: radial-gradient(circle at 50% 40%, #8fc4ea, #2d6fa8 70%, #1c4a77); }

  .footer { left: 0; top: 1110px; width: 826px; height: 90px; background: var(--footer); display: flex; align-items: center; justify-content: flex-end; padding-right: 40px; }
  .footer-web { color: var(--white); font-size: 20px; letter-spacing: 5px; font-weight: 600; white-space: nowrap; }
</style>
</head>
<body>
<main class="flyer">
  <svg class="flyer-shapes" width="826" height="1200" viewBox="0 0 826 1200">
    <defs>
      <linearGradient id="panelPhoto" x1="0" y1="0" x2="0" y2="1">
        <stop offset="0" stop-color="#9fd0f0"/>
        <stop offset="0.55" stop-color="#2f5f9a"/>
        <stop offset="0.8" stop-color="#6fae2e"/>
        <stop offset="1" stop-color="#4f8f1c"/>
      </linearGradient>
      <linearGradient id="greenPanel" x1="0" y1="0" x2="0" y2="1">
        <stop offset="0" stop-color="#a9d24a"/>
        <stop offset="1" stop-color="#6aaa22"/>
      </linearGradient>
      <linearGradient id="greenLower" x1="0" y1="0" x2="0" y2="1">
        <stop offset="0" stop-color="#8cc63f"/>
        <stop offset="1" stop-color="#4f9a1c"/>
      </linearGradient>
    </defs>

    <!-- intro band on the right -->
    <path d="M410,225 H826 V390 H360 C395,340 410,280 410,225 Z" fill="var(--blue)"/>

    <!-- solar panel photo area -->
    <path role="img" aria-label="Photo of solar panels under a blue sky above green grass"
          d="M0,0 H430 C420,230 260,400 0,430 Z" fill="url(#panelPhoto)"/>
    <path d="M430,0 C420,230 260,400 0,430" fill="none" stroke="var(--blue)" stroke-width="10"/>
    <path d="M450,0 C440,245 275,420 0,452" fill="none" stroke="var(--green)" stroke-width="6"/>

    <!-- green feature panel -->
    <path d="M0,475 C180,445 370,485 450,575 V740 H0 Z" fill="url(#greenPanel)"/>
    <path d="M0,475 C180,445 370,485 450,575" fill="none" stroke="var(--white)" stroke-width="4"/>

    <!-- blue copy band -->
    <path d="M0,740 H450 C440,810 425,860 405,900 H0 Z" fill="var(--blue)"/>

    <!-- lower green services area -->
    <path d="M0,900 H405 C445,970 455,1040 440,1110 H0 Z" fill="url(#greenLower)"/>
    <path d="M405,900 C445,970 455,1040 440,1110" fill="none" stroke="var(--blue)" stroke-width="6"/>
  </svg>

  <h1 class="block headline">Lorem ipsum</h1>
  <p class="block subline">Lorem ipsum dolor sit amet</p>
  <p class="block intro-copy">We clean residential and commercial solar panels across South Australia. Dust, bird droppings and grime cut output, so a regular clean keeps your system working at its best all year.</p>

  <p class="block contact-label">Contact us at</p>
  <p class="block contact-phone">123.456.789</p>

  <h2 class="block feature-title">Lorem<br>ipsum dolor</h2>
  <p class="block feature-copy">Our trained team uses soft brushes and pure water, with no harsh chemicals or pressure. Safe for your panels, your roof and your warranty. Ask us for a free quote today.</p>

  <div class="block brand">
    <span class="brand-mark"></span>
    <span class="brand-name">Brightfield Panel Works</span>
  </div>

  <div class="block bulb-art" role="img" aria-label="Light bulb containing a small green landscape with a house and solar panels"></div>

  <h3 class="block services-title">Lorem ipsum dolor</h3>
  <div class="block service-photo home" role="img" aria-label="Photo of a hand holding a small house model"></div>
  <div class="block service-photo roof" role="img" aria-label="Photo of a worker installing solar panels on a roof"></div>

  <footer class="block footer">
    <span class="footer-web">www.brightfieldpanelworks.com</span>
  </footer>
</main>
</body>
</html>
```